Expedition Cruise Sales Website for the Polar Regions (Antarctica & Arctic)

This will be a website for selling cruises.
This site should have a homepage, a ship page, destinations, and itineraries.
I have created a file specifying each page, and it is attached.
Pages:
1. Home
2. Cruise Lines
- 2.1 Ships
3. Destinations
- 3.1 Region - 3.2 Country - 3.3 City
4. Itineraries
- 4.1 Itinerary
5. Blog / Travel Tips 6. About Us
7. Contact
Please take a look on the attached pdf
Target Market(s)
Expedition Travelers
Coding
Coded - Design and coding required
Number of Pages Required
5+ page
Font styles to use
Look and feel
Each slider illustrates characteristics of the customer's brand and the style your logo design should communicate.

```html
<!DOCTYPE html>
<html lang="en">
<head>
<meta charset="utf-8">
<title>Norvanta.co — Cruises</title>
<link href="https://fonts.googleapis.com/css2?family=Teko:wght@400;500;600&family=Raleway:wght@400;500&family=Poppins:wght@400;500;600&display=swap" rel="stylesheet">
<style>
:root{
  --navy:#0f1e3d;
  --ink:#1b2230;
  --blue:#2e6db3;
  --blue-dark:#245a96;
  --sky:#dfeaf6;
  --sky-soft:#eef4fb;
  --teal-band:#5f8696;
  --muted:#6a7180;
  --line:#b9c3cf;
  --star:#f2a93b;
  --white:#ffffff;
  --foot:#13203f;
}
*{margin:0;padding:0;box-sizing:border-box}
html,body{width:1200px;height:4587px;overflow:hidden}
body{position:relative;background:linear-gradient(180deg,var(--sky) 730px,var(--sky-soft) 1500px,var(--sky) 2400px,#eaf2fa 3400px,var(--white) 3600px);font-family:"Raleway",sans-serif;color:var(--ink)}
.abs{position:absolute}
.teko{font-family:"Teko",sans-serif;text-transform:uppercase}
.btn{position:absolute;display:flex;align-items:center;justify-content:center;background:linear-gradient(180deg,#3a7fc8,var(--blue-dark));color:#fff;border-radius:30px;font-family:"Poppins",sans-serif;font-weight:600;font-size:12px;letter-spacing:.3px;text-transform:uppercase}
.ph{position:absolute;overflow:hidden}

/* hero */
.hero{left:0;top:0;width:1200px;height:732px;background:
  radial-gradient(ellipse 330px 210px at 82% 43%,rgba(232,238,243,.85) 0%,rgba(205,218,228,.55) 55%,rgba(205,218,228,0) 100%),
  linear-gradient(110deg,#1d4a4a 0%,#0f5f6b 30%,#1a7f8c 55%,#2f8a8e 75%,#3a5f52 100%)}
.brand{display:flex;align-items:center;gap:10px;font-family:"Poppins",sans-serif;font-weight:600;color:#fff}
.brand i{display:block;width:22px;height:22px;background:currentColor;border-radius:50%}
.nav{left:436px;top:66px;display:flex;gap:28px;font-family:"Teko",sans-serif;font-size:16px;color:#fff;text-transform:uppercase}
.nav span.on{border-bottom:1px solid #fff;padding-bottom:2px}
.contact{left:998px;top:56px;width:113px;height:40px;border-radius:20px;background:#fff;color:var(--navy);font-family:"Teko",sans-serif;font-size:16px;display:flex;align-items:center;justify-content:center;text-transform:uppercase}
.kicker{left:88px;top:268px;color:#fff;font-size:30px;display:flex;align-items:center;gap:14px}
.kicker b{display:block;width:36px;height:3px;background:#fff}
.big{left:84px;top:300px;color:#fff;font-size:170px;line-height:1;font-weight:500}
.sub{left:87px;top:448px;color:#fff;font-size:19px;line-height:21px;width:480px}
.scroll{left:88px;top:572px;width:42px;height:68px;border:2px solid #fff;border-radius:21px}
.search{left:217px;top:687px;width:766px;height:89px;background:#fff;border-radius:45px;box-shadow:0 8px 24px rgba(0,0,0,.08)}
.search span{position:absolute;left:78px;top:34px;color:#a0a6af;font-size:18px}
.search .btn{left:608px;top:22px;width:136px;height:46px;font-size:15px}

/* section headings */
.h2{width:1200px;text-align:center;font-size:44px;line-height:1;color:var(--navy);font-weight:500}
.h2s{width:1200px;text-align:center;font-size:19px;color:var(--navy)}

/* offers */
.offer{width:321px}
.offer .ph{position:relative;height:244px;border-radius:24px}
.offer h3{font-size:21px;color:var(--navy);font-weight:500;margin-top:27px}
.offer p{font-size:13px;line-height:17px;color:var(--muted);margin-top:6px;height:52px}
.offer hr{border:0;border-top:1px solid var(--line);margin-top:12px}
.price{display:flex;align-items:baseline;gap:14px;margin-top:14px;color:var(--navy)}
.price small{font-family:"Teko",sans-serif;font-size:13px;color:var(--muted);text-transform:uppercase}
.price strong{font-family:"Teko",sans-serif;font-size:34px;font-weight:500;line-height:.8}

/* destinations */
.dest{border-radius:24px;color:#fff;text-align:center}
.dest h4{position:absolute;left:0;right:0;font-family:"Teko",sans-serif;font-size:21px;font-weight:500;text-transform:uppercase}
.dest p{position:absolute;left:30px;right:30px;font-size:13px;line-height:17px}

/* cruise lines */
.band{left:0;top:2367px;width:1200px;height:557px;background:linear-gradient(90deg,#6a8fa8 0%,#82a1b4 40%,var(--teal-band) 62%)}
.line-item{left:739px;display:flex;gap:24px;color:#fff}
.line-item .ico{width:78px;height:78px;background:#fff;border-radius:6px;display:flex;align-items:center;justify-content:center}
.line-item h5{font-family:"Teko",sans-serif;font-size:21px;font-weight:500;margin-top:6px;text-transform:uppercase}
.line-item p{font-size:13px;line-height:15px;width:260px;color:#e6eef3}

/* reviews */
.rev{width:270px}
.stars{color:var(--star);font-size:18px;letter-spacing:1px}
.rev p{font-size:18px;line-height:24px;color:#3a3f48;margin-top:22px;height:104px}
.rev hr{border:0;border-top:1px solid #4c5360;margin-top:10px}
.who{display:flex;align-items:center;gap:14px;margin-top:14px;font-family:"Teko",sans-serif;font-size:20px;color:var(--navy);text-transform:uppercase}
.who b{font-family:Georgia,serif;font-size:60px;line-height:.5;color:var(--blue);height:30px}

/* closing */
.cta-kicker{left:87px;top:3566px;font-size:40px;line-height:1;font-weight:500;color:var(--navy)}
.cta-big{left:84px;top:3628px;font-size:160px;line-height:.8;font-weight:600;color:var(--navy)}
.cta-ship{left:500px;top:3500px;width:640px;height:450px;border-radius:24px;background:linear-gradient(160deg,#ffffff 0%,#e9eef3 35%,#cfd8e1 65%,#eef2f6 100%)}

/* footer */
.foot{left:0;top:3955px;width:1200px;height:566px;background:var(--foot)}
.sub-box{left:260px;top:4085px;width:680px;height:61px;background:#fff;border-radius:31px;overflow:hidden}
.sub-box span{position:absolute;left:54px;top:21px;color:#9aa0a8;font-size:14px}
.sub-box .btn{left:533px;top:0;width:147px;height:61px;border-radius:0 31px 31px 0;font-size:13px}
.col{color:#fff}
.col h6{font-family:"Teko",sans-serif;font-size:26px;font-weight:400;text-transform:uppercase;margin-bottom:8px}
.col div{font-family:"Poppins",sans-serif;font-size:12px;line-height:22px;color:#c8cfdb}
.info{left:112px;color:#d5dbe5;font-family:"Poppins",sans-serif;font-size:12px;display:flex;align-items:center;gap:12px}
.soc{left:112px;top:4402px;display:flex;gap:10px}
.soc i{display:block;width:40px;height:40px;border:1.5px solid #fff;border-radius:50%}
.soc i.on{background:var(--blue);border-color:var(--blue)}
.copy{left:0;top:4521px;width:1200px;height:66px;background:#fff;text-align:center;padding-top:24px;font-family:"Teko",sans-serif;font-size:16px;color:var(--navy);text-transform:uppercase}
</style>
</head>
<body>

<section class="hero abs" role="img" aria-label="Aerial photo of a large white cruise ship sailing turquoise coastal waters beside green hills"></section>

<div class="brand abs" style="left:88px;top:64px;font-size:22px"><i></i>Norvanta.co</div>
<nav class="nav abs">
  <span class="on">Home</span><span>Cruise Lines</span><span>Destinations</span><span>Itineraries</span><span>Blog / Travel Tips</span><span>About Us</span>
</nav>
<div class="contact abs">Contact Us</div>

<div class="kicker abs teko"><b></b>Set sail on the adventure of a<b></b></div>
<h1 class="big abs teko">Lifetime</h1>
<p class="sub abs teko">Explore breathtaking destinations, luxury cruises, and exclusive deals – only with Norvanta.co.</p>
<svg class="abs" style="left:580px;top:414px" width="36" height="36" viewBox="0 0 36 36"><path d="M18 0Q20 16 36 18Q20 20 18 36Q16 20 0 18Q16 16 18 0Z" fill="#fff"/></svg>
<svg class="abs" style="left:566px;top:490px" width="20" height="20" viewBox="0 0 36 36"><path d="M18 0Q20 16 36 18Q20 20 18 36Q16 20 0 18Q16 16 18 0Z" fill="#fff"/></svg>
<div class="scroll abs"><svg width="38" height="64" viewBox="0 0 38 64"><path d="M19 22v20M13 36l6 6 6-6" stroke="#fff" stroke-width="1.6" fill="none"/></svg></div>

<div class="search abs">
  <svg class="abs" style="left:46px;top:36px" width="18" height="18" viewBox="0 0 18 18"><circle cx="7.5" cy="7.5" r="5.5" stroke="#222" stroke-width="2" fill="none"/><path d="M12 12l4.5 4.5" stroke="#222" stroke-width="2"/></svg>
  <span>Search Cruises Now</span>
  <div class="btn">Search</div>
</div>

<h2 class="h2 abs teko" style="left:0;top:888px">Featured Offers – Limited-Time Deals</h2>
<p class="h2s abs teko" style="left:0;top:934px">Find the perfect cruise at unbeatable prices:</p>

<article class="offer abs" style="left:87px;top:998px">
  <div class="ph" role="img" aria-label="Expedition ship among icebergs and snowy Antarctic mountains" style="background:linear-gradient(180deg,#b9c6d2,#7f93a6 60%,#4e6072)"></div>
  <h3 class="teko">Best Antarctic Cruise</h3>
  <p>Sail through ice-covered landscapes, spot majestic wildlife, and experience the wonders of the polar region.</p>
  <hr><div class="price"><small>Starting from</small><strong>$4,999</strong><small>Per person</small></div>
</article>
<article class="offer abs" style="left:440px;top:998px">
  <div class="ph" role="img" aria-label="White expedition yacht near rocky Galápagos islands" style="background:linear-gradient(180deg,#9fc2dc,#5d93b8 60%,#2f6d96)"></div>
  <h3 class="teko">Top Galápagos Cruises</h3>
  <p>Witness rare wildlife, crystal-clear waters, and guided excursions in one of the world's unique destinations.</p>
  <hr><div class="price"><small>Starting from</small><strong>$3,499</strong><small>Per person</small></div>
</article>
<article class="offer abs" style="left:790px;top:998px">
  <div class="ph" role="img" aria-label="Large cruise ship at sea under a light sky" style="background:linear-gradient(180deg,#c3d4e2,#7d9fb8 55%,#3f6684)"></div>
  <h3 class="teko">Last-Minute Cruise Deals</h3>
  <p>Ready for a spontaneous adventure? Get up to 30% off select cruises—book before they're gone.</p>
  <hr><div class="price"><small>Starting from</small><strong>$4,999</strong><small>Per person</small></div>
</article>
<div class="btn" style="left:511px;top:1490px;width:178px;height:44px">View all offers</div>

<div class="ph dest" style="left:87px;top:1620px;width:383px;height:546px" role="img" aria-label="Cruise ship on turquoise Caribbean sea with palm leaves">
  <div style="position:absolute;inset:0;background:linear-gradient(180deg,#6fb3dc,#3f8cc4 45%,#2a6fa4 70%,#1d4a70)"></div>
  <h4 style="top:448px">Caribbean Paradise</h4>
  <p style="top:486px">Relax on white-sand beaches, explore tropical islands, and enjoy crystal-clear waters.</p>
</div>
<h2 class="abs teko" style="left:525px;top:1694px;font-size:44px;font-weight:500;color:var(--navy)">Explore our highlighted destinations</h2>
<p class="abs teko" style="left:525px;top:1744px;font-size:19px;color:var(--navy)">Where will your next journey take you?</p>
<div class="ph dest" style="left:488px;top:1833px;width:382px;height:333px" role="img" aria-label="Cruise ship docked in a Mediterranean bay with mountains and town">
  <div style="position:absolute;inset:0;background:linear-gradient(180deg,#8fb0c9,#6b8a8e 45%,#2f5c7a 80%,#1c3e5c)"></div>
  <h4 style="top:282px">Mediterranean Wonders</h4>
</div>
<div class="ph dest" style="left:888px;top:1833px;width:340px;height:333px;border-radius:24px 0 0 24px" role="img" aria-label="Cruise ship beside Alaskan glaciers and mountains">
  <div style="position:absolute;inset:0;background:linear-gradient(180deg,#a8c3d8,#7b9cb3 45%,#3b6686 80%,#1c3e5c)"></div>
  <h4 style="top:282px;left:0;right:40px;text-align:right">Alaskan Glaciers &amp; Wildlife</h4>
</div>
<div class="btn" style="left:511px;top:2223px;width:178px;height:45px">More destinations</div>

<section class="band abs"></section>
<div class="ph" style="left:0;top:2367px;width:712px;height:557px;background:linear-gradient(90deg,#5f8db5 0%,#9ab4c8 55%,rgba(130,161,180,0) 100%)" role="img" aria-label="Couple relaxing on the deck of a sailing boat at sea"></div>
<h2 class="abs teko" style="left:739px;top:2456px;font-size:44px;line-height:40px;font-weight:500;color:#fff">Cruise line highlights<br>travel with the best</h2>
<div class="line-item abs" style="top:2568px">
  <div class="ico"><svg width="40" height="40" viewBox="0 0 40 40" fill="none" stroke="#1b2a44" stroke-width="1.6"><rect x="8" y="4" width="12" height="30"/><path d="M20 14h10v20M4 34h32M11 9h6M11 14h6M11 19h6M11 24h6"/></svg></div>
  <div><h5>Luxury Voyages</h5><p>5-star service, gourmet dining, and world-class accommodations.</p></div>
</div>
<div class="line-item abs" style="top:2663px">
  <div class="ico"><svg width="40" height="40" viewBox="0 0 40 40" fill="none" stroke="#1b2a44" stroke-width="1.6"><path d="M20 4v6M12 10h16v10H12zM6 22l14-4 14 4-3 10H9z M4 36q4-3 8 0t8 0 8 0 8 0"/></svg></div>
  <div><h5>Adventure Cruises</h5><p>Thrilling expeditions to the world's most remote destinations.</p></div>
</div>
<div class="line-item abs" style="top:2757px">
  <div class="ico"><svg width="40" height="40" viewBox="0 0 40 40" fill="none" stroke="#1b2a44" stroke-width="1.6"><path d="M4 26h32l-5 7H9zM10 26v-6h16l4 6M14 20v-5h8v5M4 37q4-3 8 0t8 0 8 0 8 0"/></svg></div>
  <div><h5>Family-Friendly Cruises</h5><p>Onboard entertainment, kids' activities, and spacious cabins.</p></div>
</div>
<div class="btn" style="left:511px;top:2905px;width:178px;height:43px">See all cruise lines</div>

<h2 class="h2 abs teko" style="left:0;top:3104px;line-height:44px">What our travelers say – real<br>customer reviews</h2>
<div class="rev abs" style="left:132px;top:3228px">
  <div class="stars">★★★★★</div>
  <p>"An unforgettable experience! The ship was luxurious, and the destinations were beyond stunning."</p>
  <hr><div class="who"><b>“</b>– Clara M.</div>
</div>
<div class="rev abs" style="left:463px;top:3228px">
  <div class="stars">★★★★★</div>
  <p>"Our family had the best vacation ever! Everything was so well planned, and the service was top-notch."</p>
  <hr><div class="who"><b>“</b>– The Whitfields</div>
</div>
<div class="rev abs" style="left:774px;top:3228px">
  <div class="stars">★★★★★</div>
  <p>"I booked a last-minute deal, and it was the best decision ever! Amazing value for such a fantastic trip."</p>
  <hr><div class="who"><b>“</b>– Daniel K.</div>
</div>

<div class="ph cta-ship" role="img" aria-label="Large white cruise ship bow rising from splashing water"></div>
<h3 class="cta-kicker abs teko">Ready to set sail?</h3>
<h2 class="cta-big abs teko">Cruise</h2>
<p class="abs teko" style="left:87px;top:3754px;width:400px;font-size:19px;line-height:20px;color:var(--navy)">Your perfect cruise is waiting. Explore, book, and get ready for an adventure of a lifetime.</p>
<div class="btn" style="left:89px;top:3809px;width:207px;height:44px">Find your cruise now</div>

<footer class="foot abs"></footer>
<div class="sub-box abs">
  <svg class="abs" style="left:28px;top:24px" width="16" height="13" viewBox="0 0 16 13"><rect x=".5" y=".5" width="15" height="12" rx="1" fill="#9aa0a8"/><path d="M1 1l7 6 7-6" stroke="#fff" fill="none"/></svg>
  <span>Enter email address</span>
  <div class="btn">Subscribe</div>
</div>

<div class="brand abs" style="left:112px;top:4226px;font-size:38px;color:#fff"><i style="width:44px;height:44px;background:var(--blue)"></i>Norvanta.co</div>
<div class="info abs" style="top:4312px"><svg width="12" height="12" viewBox="0 0 12 12"><path d="M2 1l2.5 0 1 3-1.5 1q1 2 3 3l1-1.5 3 1v2.5q-6 .5-9-9z" fill="#fff"/></svg>555-018-2244</div>
<div class="info abs" style="top:4338px"><svg width="12" height="10" viewBox="0 0 12 10"><rect width="12" height="10" rx="1" fill="#fff"/><path d="M0 1l6 4 6-4" stroke="#13203f" fill="none"/></svg>hello@norvanta.example</div>
<div class="info abs" style="top:4364px"><svg width="12" height="12" viewBox="0 0 12 12"><circle cx="6" cy="6" r="6" fill="#fff"/><path d="M6 3v3.5h2.5" stroke="#13203f" fill="none"/></svg>09:00 - 19:00</div>
<div class="soc abs"><i></i><i></i><i class="on"></i><i></i><i></i></div>

<div class="col abs" style="left:493px;top:4222px"><h6>Destinations</h6><div>Indian Ocean<br>Middle East<br>Europe<br>Caribbean &amp; Mexico<br>Far East<br>North America<br>Africa<br>Australasia<br>Cruise</div></div>
<div class="col abs" style="left:717px;top:4222px"><h6>Company</h6><div>Contact Us<br>About Us<br>Meet Our Concierge<br>Careers<br>Travel Insurance<br>Holiday Extras<br>FAQs</div></div>
<div class="col abs" style="left:913px;top:4222px"><h6>Legal</h6><div>Booking Terms &amp; Conditions<br>Visa Information<br>Your Key Rights<br>Modern Slavery Statement<br>Privacy Policy<br>Cookie Policy<br>Sitemap</div></div>

<div class="copy abs">© Norvanta.co 2025. All rights reserved</div>

</body>
</html>
```